Harbor Elder Guides (HEG) business card and logo

I need a business card and logo that stands out of the crowd!!! This business is a health care placement agency. I need it to show confidence and compassion BUT be very modern please. I want the back with the information side to look like the black card and the color palette inspiration is the blue and rose gold the top photo is the logo inspiration idea! But I’m open to other things.
Updates

I have a picture of the color design that I want my business card to have- Designers, would you also mock up the color with the business card. I would like to see that blue hue and rose gold variation so that I can get a really good picture.

Industry/Entity Type

Healthcare placement agency- client based business, meeting and touring businesses with clients.

Contact Information for Business Card

I’ve given a photo inspiration for the back of the card, the how to reach me section. I’m wanting to have a QR code placed, room for email, phone, website.

Font styles to use
Script
Other font styles liked:
• Open to many design options- I do want clean but a bit soft and relatable

Requirements
Must have
• Brand expansion ability, either an acronym as the logo, the E possibly, or the design needs to have a sleek, confident modern feel.
Nice to have
• QR code, ability to have raised texture in the background of the card for an extra flair and look, but not too in your face.

```html
<!DOCTYPE html>
<html lang="en">
<head>
<meta charset="utf-8">
<title>Harbor Elder Guides – Business Card</title>
<link href="https://fonts.googleapis.com/css2?family=Archivo:wght@400;500;700&display=swap" rel="stylesheet">
<style>
  :root{
    --backdrop:#a0a4b9;
    --card-navy:#252a46;
    --rose-gold:#d9a88c;
    --soft-white:#d4d6e2;
    --shadow:rgba(30,32,55,.35);
  }
  *{margin:0;padding:0;box-sizing:border-box}
  html,body{width:674px;height:1200px;overflow:hidden}
  body{
    background:var(--backdrop);
    font-family:"Archivo",Helvetica,Arial,sans-serif;
    position:relative;
  }
  .card{
    position:absolute;left:77px;width:520px;height:297px;
    background:var(--card-navy);
    box-shadow:14px 22px 30px var(--shadow);
  }
  .card--front{top:230px}
  .card--back{top:650px}

  .brand{display:flex;align-items:center;position:absolute}
  .brand__mark{border:1.5px solid var(--rose-gold);border-radius:50%;flex:none}
  .brand__name{
    color:var(--rose-gold);font-weight:500;text-transform:uppercase;line-height:1.05;
  }
  .card--front .brand{left:50%;top:50%;transform:translate(-50%,-50%);gap:22px}
  .card--front .brand__mark{width:54px;height:54px}
  .card--front .brand__name{font-size:19px;letter-spacing:.02em}

  .card--back .brand{right:45px;top:45px;gap:12px}
  .card--back .brand__mark{width:30px;height:30px}
  .card--back .brand__name{font-size:11px;letter-spacing:.02em}

  .holder{position:absolute;left:45px;top:52px}
  .holder__name{color:var(--rose-gold);font-weight:700;font-size:17px;letter-spacing:.01em}
  .holder__title{color:var(--soft-white);font-size:10.5px;letter-spacing:.02em;margin-top:1px}

  .contact,.address{
    position:absolute;bottom:44px;color:var(--soft-white);
    font-size:11px;line-height:1.45;text-transform:uppercase;letter-spacing:.01em;
  }
  .contact{left:45px}
  .contact__sep{opacity:.6;margin:0 4px}
  .address{right:45px}
</style>
</head>
<body>
  <section class="card card--front" aria-label="Card front">
    <div class="brand">
      <span class="brand__mark"></span>
      <p class="brand__name">Harbor<br>Elder<br>Guides</p>
    </div>
  </section>

  <section class="card card--back" aria-label="Card back">
    <div class="holder">
      <p class="holder__name">MARA QUILLEN</p>
      <p class="holder__title">MANAGING DIRECTOR</p>
    </div>
    <div class="brand">
      <span class="brand__mark"></span>
      <p class="brand__name">Harbor<br>Elder<br>Guides</p>
    </div>
    <p class="contact">555.018.2046<span class="contact__sep">/</span>MARA@HARBORELDER.COM<br>WWW.HARBORELDER.COM</p>
    <p class="address">418 LARKSPUR LANE<br>MARLOW, GA 30199</p>
  </section>
</body>
</html>
```